Redesign - Trifold Brochure - Adding new and fresh look.

I have attached what we currently have as a brochure but we need it to be redesigned. The information content is accurate but looking for fresh new design/layout. Please see the images attached. In tif and pdf format. If you need a different format to work please specify and will do my best to upload it.

Target Market(s)

Retail giveaways to educate customers.

Requirements
Must have
• New fresh look

```html
<!DOCTYPE html>
<html lang="en">
<head>
<meta charset="utf-8">
<title>How Does CBD Work In Your Body? – Brochure Panel</title>
<link href="https://fonts.googleapis.com/css2?family=Roboto+Condensed:wght@300;400;700&display=swap" rel="stylesheet">
<style>
  :root {
    --forest: #17241a;
    --paper: #ffffff;
    --lime: #9cc33b;
    --lime-light: #cfe27a;
    --lime-dark: #6f9a22;
    --orange: #f4a21f;
    --ink: #1e1e1e;
    --ink-soft: #3a3a3a;
  }
  * { box-sizing: border-box; margin: 0; padding: 0; }
  html, body { width: 1200px; height: 956px; overflow: hidden; background: #e9e9e9; }
  body { font-family: "Roboto Condensed", sans-serif; color: var(--ink); }

  .brochure { position: relative; width: 1200px; height: 956px; background: var(--forest); overflow: hidden; }

  .intro-panel { position: absolute; left: 0; top: 0; width: 407px; height: 956px; background: var(--paper); }

  .top-decor { position: absolute; left: 0; top: 0; width: 560px; height: 480px; }

  .info-panel {
    position: absolute; left: 428px; top: 22px; width: 750px; height: 911px;
    background: linear-gradient(180deg, #c0c1ba 0%, #c7c8c0 70%, #d9dcbc 100%);
    overflow: hidden;
  }
  .info-panel .panel-decor { position: absolute; inset: 0; }

  .banner {
    position: absolute; display: flex; align-items: center; justify-content: center;
    font-weight: 700; color: var(--ink);
    background: linear-gradient(90deg, var(--lime-dark) 0%, var(--lime) 35%, var(--lime-light) 100%);
  }
  .banner--title {
    left: 453px; top: 68px; width: 700px; height: 46px; font-size: 29px;
    clip-path: polygon(0 0, 100% 0, 95% 100%, 5% 100%);
  }
  .banner--side {
    left: 38px; width: 344px; height: 35px; font-size: 17px;
    clip-path: polygon(0 0, 100% 0, 91% 100%, 9% 100%);
  }

  .body-copy { position: absolute; text-align: center; font-weight: 300; color: var(--ink-soft); }
  .body-copy--intro { left: 455px; top: 134px; width: 695px; font-size: 17px; line-height: 21.8px; }
  .body-copy--what { left: 43px; top: 540px; width: 336px; font-size: 16px; line-height: 21.8px; color: var(--ink); }

  .diagram {
    position: absolute; left: 464px; top: 312px; width: 680px; height: 467px;
    border: 3px solid #fff; border-radius: 20px; overflow: hidden;
    background:
      radial-gradient(ellipse 45% 55% at 74% 52%, #e7551f 0%, #b52a1c 35%, rgba(90,30,30,0) 75%),
      radial-gradient(ellipse 50% 60% at 55% 45%, rgba(240,180,70,.55) 0%, rgba(240,180,70,0) 60%),
      radial-gradient(ellipse 35% 70% at 20% 55%, #2b8ca0 0%, #134552 45%, rgba(10,30,40,0) 80%),
      linear-gradient(90deg, #0c2a33 0%, #15323a 40%, #4a2622 75%, #2a1513 100%);
  }
  .diagram .figure-area { position: absolute; left: 70px; top: 15px; width: 170px; height: 445px; }
  .brain-frame {
    position: absolute; left: 425px; top: 144px; width: 216px; height: 202px;
    border: 3px solid #f6e7a8; border-radius: 22px;
    box-shadow: 0 0 10px rgba(255,230,150,.6);
  }
  .diagram-lines { position: absolute; inset: 0; }
  .callout {
    position: absolute; background: var(--lime); color: var(--ink); border-radius: 3px;
    font-size: 10.5px; line-height: 13.5px; text-align: center;
    display: flex; align-items: center; justify-content: center; padding: 4px 6px;
  }

  .benefits-lead { position: absolute; left: 428px; top: 792px; width: 750px; text-align: center; font-size: 17px; font-weight: 700; color: var(--ink); }
  .nutrient { position: absolute; top: 834px; font-size: 17px; font-weight: 700; line-height: 22px; }
  .nutrient .label { position: absolute; left: 0; top: 0; color: var(--ink); white-space: nowrap; }
  .nutrient ul { list-style: none; color: #4a4a40; }
  .nutrient--high { left: 500px; }
  .nutrient--high ul { margin-left: 66px; }
  .nutrient--low { left: 839px; }
  .nutrient--low ul { margin-left: 61px; }

  .relief-list { position: absolute; left: 18px; top: 798px; width: 386px; list-style: none; font-size: 17px; font-weight: 700; }
  .relief-row { display: flex; justify-content: center; gap: 12px; height: 22px; margin-bottom: 17px; }
  .relief-row span { display: flex; align-items: center; gap: 6px; white-space: nowrap; }
  .tick { width: 19px; height: 19px; flex: none; }
</style>
</head>
<body>
<main class="brochure">

  <section class="intro-panel">
    <h2 class="banner banner--side" style="top:479px;">What is CBD?</h2>
    <p class="body-copy body-copy--what">CBD stands for Canna-bi-dy-all. CBD is one of many compounds called phytocan-nabinoids that is found in various plant species. The industrial hemp plant is a plentiful source of CBD. When derived from industrial hemp, CBD with less than 0.03% THC by weight has no psychoactive properties but retains all of its positive bio</p>
    <h2 class="banner banner--side" style="top:744px;">CBD is commonly used as relief from:</h2>
    <div class="relief-list">
      <div class="relief-row">
        <span><svg class="tick" viewBox="0 0 20 20" aria-hidden="true"><circle cx="10" cy="10" r="8" fill="none" stroke="#1e1e1e" stroke-width="1.6"/><path d="M6 10 L9.5 13.5 L18 3" fill="none" stroke="#1e1e1e" stroke-width="1.8"/></svg>Pain</span>
        <span><svg class="tick" viewBox="0 0 20 20" aria-hidden="true"><circle cx="10" cy="10" r="8" fill="none" stroke="#1e1e1e" stroke-width="1.6"/><path d="M6 10 L9.5 13.5 L18 3" fill="none" stroke="#1e1e1e" stroke-width="1.8"/></svg>Inflammation</span>
        <span><svg class="tick" viewBox="0 0 20 20" aria-hidden="true"><circle cx="10" cy="10" r="8" fill="none" stroke="#1e1e1e" stroke-width="1.6"/><path d="M6 10 L9.5 13.5 L18 3" fill="none" stroke="#1e1e1e" stroke-width="1.8"/></svg>Anxiety</span>
      </div>
      <div class="relief-row">
        <span><svg class="tick" viewBox="0 0 20 20" aria-hidden="true"><circle cx="10" cy="10" r="8" fill="none" stroke="#1e1e1e" stroke-width="1.6"/><path d="M6 10 L9.5 13.5 L18 3" fill="none" stroke="#1e1e1e" stroke-width="1.8"/></svg>Sleep Disorders</span>
        <span><svg class="tick" viewBox="0 0 20 20" aria-hidden="true"><circle cx="10" cy="10" r="8" fill="none" stroke="#1e1e1e" stroke-width="1.6"/><path d="M6 10 L9.5 13.5 L18 3" fill="none" stroke="#1e1e1e" stroke-width="1.8"/></svg>Neurological Disorders</span>
      </div>
      <div class="relief-row">
        <span><svg class="tick" viewBox="0 0 20 20" aria-hidden="true"><circle cx="10" cy="10" r="8" fill="none" stroke="#1e1e1e" stroke-width="1.6"/><path d="M6 10 L9.5 13.5 L18 3" fill="none" stroke="#1e1e1e" stroke-width="1.8"/></svg>Opiate Dependence</span>
      </div>
    </div>
  </section>

  <svg class="top-decor" viewBox="0 0 560 480" aria-hidden="true">
    <defs>
      <linearGradient id="oil-tones" x1="0" y1="0" x2="1" y2="1">
        <stop offset="0" stop-color="#c9961e"/>
        <stop offset=".35" stop-color="#b5b43a"/>
        <stop offset=".7" stop-color="#7e8f2a"/>
        <stop offset="1" stop-color="#3d5a1e"/>
      </linearGradient>
    </defs>
    <path d="M0 0 H500 C505 150 480 290 400 360 C300 440 150 445 0 430 Z" fill="#f4a21f"/>
    <path d="M0 0 H470 C476 150 455 270 385 330 C290 400 150 412 0 405 Z" fill="#a8c934"/>
    <path d="M0 0 H427 C432 110 422 175 404 207 C370 280 300 330 200 362 C130 380 60 385 0 380 Z" fill="url(#oil-tones)" role="img" aria-label="Close-up photo of golden CBD oil dripping into glass droplets"/>
  </svg>

  <section class="info-panel">
    <svg class="panel-decor" viewBox="0 0 750 911" preserveAspectRatio="none" aria-hidden="true">
      <path d="M0 0 H70 C60 120 90 230 120 300 C70 240 20 150 0 120 Z" fill="#fbf6dd" opacity=".9"/>
      <path d="M0 0 H28 C22 90 50 190 110 300 C50 230 10 140 0 95 Z" fill="#ffffff"/>
      <path d="M750 540 C700 620 640 760 560 840 C480 900 420 911 400 911 H750 Z" fill="#e9efb8" opacity=".8"/>
      <path d="M750 700 C690 800 560 890 430 911 H750 Z" fill="#a7c93d"/>
      <path d="M750 690 C700 760 640 820 560 870 C650 840 710 790 750 740 Z" fill="#fbfbe8"/>
    </svg>
  </section>

  <h1 class="banner banner--title">How Does CBD Work In Your Body?</h1>

  <p class="body-copy body-copy--intro">Your body produces certain natural compounds called cannabinoids that are used to regulate functions for your entire body. Inside your body there is a processing network for cannabinoids called your Endo-cannabinoid System. CBD mimics the natural cannabinoids produced by your body and stimulates certain receptors found on the surface of cells in your body that effect your ECS. These cells are mainly located in the central nervous system and the immune system. This reaction caused by the in&#8209;troduction of CBD helps balance and maintain and restore your body’s natural function. Essentially</p>

  <figure class="diagram">
    <div class="figure-area" role="img" aria-label="Glowing blue illustration of a human body network"></div>
    <div class="brain-frame" role="img" aria-label="Glowing red and orange illustration of a brain"></div>
    <svg class="diagram-lines" viewBox="0 0 680 467" aria-hidden="true">
      <g stroke="#e8f0d0" stroke-width="1.2" fill="none">
        <path d="M232 110 H180"/>
        <path d="M382 110 L410 140 H430"/>
        <path d="M232 230 H180 V275"/>
        <path d="M382 230 H425"/>
        <path d="M232 407 H190"/>
        <path d="M382 407 L404 380 H453"/>
      </g>
    </svg>
    <div class="callout" style="left:232px;top:79px;width:149px;height:58px;">CB2 receptors are predominantly found in the immune system.</div>
    <div class="callout" style="left:232px;top:196px;width:149px;height:66px;">CB1 and CB2 receptors are found on the surface of cells in your body that effect your endocanna-binoid system.</div>
    <div class="callout" style="left:232px;top:370px;width:149px;height:66px;">CB2 receptors are responsible for the regulation of inflamma-tion which in turn reduces pain.</div>
    <div class="callout" style="left:453px;top:347px;width:184px;height:86px;">CB1 receptors are found primarily in the brain controlling memory processing, motor regulation, appetite, pain sensation, mood, and sleep.</div>
  </figure>

  <p class="benefits-lead">There are many other benefits from using CBD and hemp products. Hemp products are:</p>
  <div class="nutrient nutrient--high">
    <span class="label">High In :</span>
    <ul><li>Omega 3 and 6 Fatty Acids</li><li>Vitamins A &amp; E</li><li>Calcium, Iron &amp; Antioxidants</li></ul>
  </div>
  <div class="nutrient nutrient--low">
    <span class="label">Low In:</span>
    <ul><li>Saturated Fats</li><li>Cholesterol</li><li>Carbohydrates</li></ul>
  </div>

</main>
</body>
</html>
```